Bref créative
Business Cards & stationery for Drywall Contractor
Business card, invoice, fax, letterhead, envelopes
Professional
Radoslav Benek
Owner
N/A - We do not want our address on the business card
info@tmkbuildingworks.example
www.tmkbuildingworks.example
SCC284730592
"Certified Specialty Contractor"
Framing; Drywall Installation & Finishing; Wall Textures; Acoustical Ceilings; Raised Access Floors; Commercial & Residential; New Construction;
Remodeling

```html
<!DOCTYPE html>
<html lang="en">
<head>
<meta charset="utf-8">
<title>TMK Construction — Stationery Set</title>
<link href="https://fonts.googleapis.com/css2?family=Open+Sans:wght@400;700;800&display=swap" rel="stylesheet">
<style>
:root{
  --red:#c4161c;
  --red-dark:#9e1015;
  --ink:#2b2b2b;
  --grey:#8a8a8a;
  --line:#e2e2e2;
  --paper:#ffffff;
  --bg:#ecebe8;
  --faint:#f3e3e3;
}
*{box-sizing:border-box;margin:0;padding:0}
html,body{width:1200px;height:271px;overflow:hidden;background:var(--bg);font-family:"Open Sans",Arial,sans-serif;color:var(--ink)}
.canvas{position:relative;width:1200px;height:271px}
.sheet{position:absolute;background:var(--paper);box-shadow:0 1px 4px rgba(0,0,0,.18)}
.brand{display:flex;align-items:center;gap:3px;font-weight:800;color:var(--red);letter-spacing:.2px;white-space:nowrap}
.brand .mark{width:7px;height:7px;background:var(--red)}
.brand.light{color:#fff}
.brand.light .mark{background:#fff}
.footer-band{position:absolute;left:0;right:0;bottom:0;height:4px;background:var(--red)}
.tiny{font-size:3.4px;line-height:5px;color:var(--grey)}
.watermark{position:absolute;left:0;right:0;top:42%;text-align:center;font-weight:800;font-size:40px;color:var(--faint)}
/* business cards */
.card{left:12px;width:104px;height:60px}
.card.front{top:96px}
.card.back{top:166px;background:#1e1e1e}
.card .brand{position:absolute;left:8px;top:10px;font-size:7px}
.card .person{position:absolute;left:8px;top:28px;font-size:5px;font-weight:700}
.card .role{position:absolute;left:8px;top:35px;font-size:3.8px;color:var(--grey)}
.card .contact{position:absolute;left:8px;bottom:8px}
.card.back .brand{left:28px;top:24px;font-size:7px}
.card.back .footer-band{height:3px}
/* letterhead & fax */
.letter{top:12px;width:132px;height:240px}
.letter .brand{position:absolute;left:10px;top:12px;font-size:7px}
.letter .meta{position:absolute;right:10px;top:12px;text-align:right}
.letter .rule{position:absolute;left:10px;right:10px;top:30px;height:1px;background:var(--red)}
.letter .foot{position:absolute;left:10px;right:10px;bottom:8px;text-align:center}
.fax-grid{position:absolute;left:10px;right:10px;top:36px;display:grid;grid-template-columns:1fr 1fr;gap:3px 6px}
.fax-grid span{height:5px;border-bottom:1px solid var(--line);font-size:3.4px;color:var(--grey)}
/* invoice */
.invoice{left:432px;top:12px;width:132px;height:240px}
.invoice .brand{position:absolute;left:10px;top:12px;font-size:7px}
.invoice h2{position:absolute;right:10px;top:11px;font-size:8px;color:var(--red);font-weight:800}
.invoice table{position:absolute;left:10px;right:10px;top:40px;width:112px;border-collapse:collapse;font-size:3.4px}
.invoice th{background:var(--red);color:#fff;height:6px;text-align:left;padding-left:2px;font-weight:700}
.invoice td{height:7px;border:1px solid var(--line)}
/* envelopes */
.env{position:absolute;background:var(--paper);box-shadow:0 1px 4px rgba(0,0,0,.2)}
.env svg{position:absolute;left:0;top:0}
.env .brand{position:absolute;left:8px;top:8px;font-size:6px}
.env.red-flap{left:588px;top:72px;width:156px;height:60px}
.env.dark-flap{left:628px;top:108px;width:160px;height:82px}
.env.plain{left:600px;top:180px;width:216px;height:62px}
.env.plain .brand{position:relative;left:auto;top:auto}
.env.plain .head{position:absolute;left:8px;top:8px}
.env.plain .footer-band{height:3px}
/* folder */
.folder{position:absolute;top:12px;height:240px}
.folder.inside{left:828px;width:178px;background:var(--red)}
.folder.cover{left:1008px;width:180px;background:var(--red)}
.folder .pocket{position:absolute;left:0;right:0;bottom:0;height:86px;background:var(--red-dark)}
.folder .card-slot{position:absolute;right:22px;bottom:60px;width:46px;height:26px;border:1px solid rgba(255,255,255,.55)}
.folder .cover-panel{position:absolute;left:20px;right:20px;top:70px;height:56px;background:#fff;display:flex;align-items:center;justify-content:center}
.folder .cover-panel .brand{font-size:11px}
.folder .cover-foot{position:absolute;left:0;right:0;bottom:14px;text-align:center;color:#fff;font-size:4px}
</style>
</head>
<body>
<main class="canvas">

  <!-- business cards -->
  <section class="sheet card front">
    <div class="brand"><span class="mark"></span>TMK CONSTRUCTION</div>
    <p class="person">Radoslav Benek</p>
    <p class="role">Owner · Certified Specialty Contractor</p>
    <div class="contact tiny">
      <p>info@tmkbuildingworks.example</p>
      <p>www.tmkbuildingworks.example</p>
      <p>SCC284730592 · (555) 610-2290</p>
    </div>
    <div class="footer-band"></div>
  </section>
  <section class="sheet card back">
    <div class="brand light"><span class="mark"></span>TMK CONSTRUCTION</div>
    <div class="footer-band"></div>
  </section>

  <!-- letterhead -->
  <section class="sheet letter" style="left:132px">
    <div class="brand"><span class="mark"></span>TMK CONSTRUCTION</div>
    <div class="meta tiny"><p>(555) 610-2290</p><p>info@tmkbuildingworks.example</p></div>
    <div class="rule"></div>
    <div class="watermark">TMK</div>
    <p class="foot tiny">1420 Cedar Ridge Rd, Austin TX · www.tmkbuildingworks.example</p>
    <div class="footer-band"></div>
  </section>

  <!-- fax -->
  <section class="sheet letter" style="left:288px">
    <div class="brand"><span class="mark"></span>TMK CONSTRUCTION</div>
    <div class="meta tiny"><p>FAX</p><p>(555) 610-2291</p></div>
    <div class="rule"></div>
    <div class="fax-grid">
      <span>To:</span><span>From:</span>
      <span>Fax:</span><span>Pages:</span>
      <span>Phone:</span><span>Date:</span>
      <span>Re:</span><span>CC:</span>
    </div>
    <div class="watermark">TMK</div>
    <p class="foot tiny">1420 Cedar Ridge Rd, Austin TX · www.tmkbuildingworks.example</p>
    <div class="footer-band"></div>
  </section>

  <!-- invoice -->
  <section class="sheet invoice">
    <div class="brand"><span class="mark"></span>TMK CONSTRUCTION</div>
    <h2>INVOICE</h2>
    <table>
      <thead><tr><th>Qty</th><th>Description</th><th>Price</th><th>Total</th></tr></thead>
      <tbody>
        <tr><td></td><td></td><td></td><td></td></tr><tr><td></td><td></td><td></td><td></td></tr>
        <tr><td></td><td></td><td></td><td></td></tr><tr><td></td><td></td><td></td><td></td></tr>
        <tr><td></td><td></td><td></td><td></td></tr><tr><td></td><td></td><td></td><td></td></tr>
        <tr><td></td><td></td><td></td><td></td></tr><tr><td></td><td></td><td></td><td></td></tr>
        <tr><td></td><td></td><td></td><td></td></tr><tr><td></td><td></td><td></td><td></td></tr>
        <tr><td></td><td></td><td></td><td></td></tr><tr><td></td><td></td><td></td><td></td></tr>
        <tr><td></td><td></td><td></td><td></td></tr><tr><td></td><td></td><td></td><td></td></tr>
        <tr><td></td><td></td><td></td><td></td></tr><tr><td></td><td></td><td></td><td></td></tr>
      </tbody>
    </table>
    <div class="footer-band"></div>
  </section>

  <!-- envelopes -->
  <section class="env red-flap">
    <svg width="156" height="60" viewBox="0 0 156 60"><polygon points="0,0 156,0 78,30" fill="var(--red)"/></svg>
  </section>
  <section class="env dark-flap">
    <svg width="160" height="82" viewBox="0 0 160 82"><polygon points="0,0 160,0 80,38" fill="#1e1e1e"/></svg>
  </section>
  <section class="env plain">
    <div class="head">
      <div class="brand"><span class="mark"></span>TMK CONSTRUCTION</div>
      <p class="tiny">1420 Cedar Ridge Rd, Austin TX</p>
    </div>
    <div class="footer-band"></div>
  </section>

  <!-- presentation folder -->
  <section class="folder inside">
    <div class="pocket"></div>
    <div class="card-slot"></div>
  </section>
  <section class="folder cover">
    <div class="cover-panel"><div class="brand"><span class="mark"></span>TMK CONSTRUCTION</div></div>
    <p class="cover-foot">www.tmkbuildingworks.example</p>
  </section>

</main>
</body>
</html>
```